" Dentista, especialista em Ortodontia. Professor Universitário, com titulaçao de excelência (Doutor). Atua em consultório particular atuando em uma odontologia de excelência, correçao dos dentes através de aparelhos dentários e reabilitaçao oral com técnicas de altíssimo nível em um ambiente diferenciado. Profissional qualificado e bem conceituado no mercado de trabalho. Possui uma logo, feita por um amador, a qual tive a infelicidade de descobrir que foi clonada de um profissional americano. "

```html
<!DOCTYPE html>
<html lang="pt-BR">
<head>
<meta charset="utf-8">
<title>Cartão de visita – Dr. Rafael Monteiro, Ortodontista</title>
<link rel="stylesheet" href="https://fonts.googleapis.com/css2?family=Ubuntu:wght@400;500;700&display=swap">
<style>
  :root {
    --backdrop: #e9e6e2;
    --card-top: #ffffff;
    --card-bottom: #eceeef;
    --frame: #3f9ea6;
    --frame-light: #8fcbd0;
    --navy: #1f3d5c;
    --teal: #3a9aa3;
    --ink: #1c2a36;
    --mark: #3f9ea6;
  }
  * { box-sizing: border-box; margin: 0; padding: 0; }
  html, body {
    width: 1200px; height: 1200px; overflow: hidden;
    background: var(--backdrop);
    font-family: "Ubuntu", sans-serif;
  }
  .business-card {
    position: absolute;
    left: 100px; top: 214px;
    width: 1000px; height: 773px;
    border-radius: 70px;
    border: 14px solid var(--frame);
    box-shadow: inset 0 0 0 4px var(--frame-light), 0 18px 40px rgba(0,0,0,0.18);
    background: linear-gradient(180deg, var(--card-top) 0%, var(--card-top) 55%, var(--card-bottom) 100%);
    text-align: center;
    color: var(--ink);
  }
  .card-content {
    position: absolute; left: 0; right: 0; top: 0; bottom: 0;
  }
  .brand-dot {
    position: absolute; left: 50%; top: 100px;
    width: 110px; height: 110px; margin-left: -55px;
    border-radius: 50%;
    background: var(--mark);
  }
  .doctor-name {
    position: absolute; left: 0; right: 0; top: 236px;
    font-weight: 700; font-size: 44px; color: var(--navy);
    letter-spacing: 0.5px;
  }
  .specialty {
    position: absolute; left: 0; right: 0; top: 298px;
    font-weight: 400; font-size: 30px; color: var(--teal);
    letter-spacing: 17px; padding-left: 17px;
  }
  .registration {
    position: absolute; left: 0; right: 0; top: 346px;
    font-weight: 700; font-size: 22px; color: var(--navy);
    letter-spacing: 2px;
  }
  .contact-icon {
    position: absolute; left: 50%;
    transform: translateX(-50%);
    color: var(--ink);
  }
  .contact-icon.email-icon { top: 376px; font-size: 40px; font-weight: 500; }
  .contact-icon.phone-icon { top: 480px; width: 30px; height: 50px; }
  .email {
    position: absolute; left: 0; right: 0; top: 428px;
    font-size: 32px; color: var(--ink);
  }
  .phone {
    position: absolute; left: 0; right: 0;
    font-size: 34px; color: var(--ink); letter-spacing: 1px;
  }
  .phone.primary { top: 540px; }
  .phone.secondary { top: 597px; }
</style>
</head>
<body>
  <main class="business-card">
    <div class="card-content">
      <span class="brand-dot" aria-hidden="true"></span>
      <h1 class="doctor-name">Dr. Rafael Monteiro</h1>
      <p class="specialty">ORTODONTISTA</p>
      <p class="registration">CRO - SP 48312-7</p>

      <span class="contact-icon email-icon" aria-hidden="true">@</span>
      <p class="email">rafaelmonteiro@mailbox.com</p>

      <svg class="contact-icon phone-icon" viewBox="0 0 30 50" aria-hidden="true">
        <rect x="3" y="2" width="24" height="46" rx="4" fill="none" stroke="var(--ink)" stroke-width="3"/>
        <line x1="3" y1="38" x2="27" y2="38" stroke="var(--ink)" stroke-width="2.5"/>
        <circle cx="15" cy="43" r="2" fill="var(--ink)"/>
      </svg>
      <p class="phone primary">11 4821-3067</p>
      <p class="phone secondary">11 4830-5192</p>
    </div>
  </main>
</body>
</html>
```